Looking for a contemporary business card design with our logo

would like to consider a embossing look although I'm not married to the idea. We are a custom jeweler that needs a look that represents old world craftsmanship with a modern twist that's why we went with a more modern shield type of logo that can be stamped inside our rings.
It could be two sided or one we are more after a look the pops and is trendy and creative. (WE ARE NOT LOOKING FOR A COOKIE CUTTER LAYOUT)
We have attached the image and will be using the logo with harwick studio wording in the format that it's in unless you see a better way of doing it.
If the logo needs a twist we are O.K. with suggestions as well.
This card should scream "Quality" from a high end studio.
Harwick Studio
4186 Maplecrest Rd. Unit B-2
Brookvale, WY 80317
www.harwickstudio-example.com
lu@harwickstudio-example.com
Should speak quality craftsmanship

```html
<!DOCTYPE html>
<html lang="en">
<head>
<meta charset="utf-8">
<title>Harwick Studio – Business Card</title>
<link rel="stylesheet" href="https://fonts.googleapis.com/css2?family=Arimo:wght@400;700&display=swap">
<style>
  :root {
    --page-bg: #e9e9e7;
    --card-white: #ffffff;
    --card-black: #0b0b0b;
    --ink-dark: #111111;
    --ink-light: #ffffff;
  }
  * { margin: 0; padding: 0; box-sizing: border-box; }
  html, body {
    width: 1200px;
    height: 2568px;
    overflow: hidden;
    background: var(--page-bg);
    font-family: "Arimo", Arial, sans-serif;
  }
  .business-card {
    position: absolute;
    left: 50px;
    top: 970px;
    width: 1100px;
    height: 628px;
    background: var(--card-white);
    overflow: hidden;
    box-shadow: 0 6px 24px rgba(0,0,0,0.12);
  }
  .diagonal-band {
    position: absolute;
    inset: 0;
    width: 100%;
    height: 100%;
  }
  .diagonal-band polygon { fill: var(--card-black); }
  .brand-mark {
    position: absolute;
    left: 70px;
    top: 96px;
    display: flex;
    align-items: center;
    gap: 22px;
  }
  .brand-square {
    width: 120px;
    height: 120px;
    border: 10px solid var(--ink-dark);
  }
  .brand-name {
    font-size: 52px;
    font-weight: 400;
    line-height: 1.05;
    color: var(--ink-dark);
    letter-spacing: -0.5px;
  }
  .contact-block {
    position: absolute;
    right: 62px;
    top: 318px;
    text-align: right;
    color: var(--ink-light);
  }
  .company-name {
    font-size: 30px;
    font-weight: 700;
    margin-bottom: 38px;
    padding-right: 50px;
  }
  .contact-row {
    display: flex;
    justify-content: flex-end;
    align-items: center;
    gap: 20px;
    font-size: 24px;
    font-weight: 400;
    line-height: 1.35;
  }
  .contact-row + .contact-row { margin-top: 8px; }
  .address-lines { text-align: right; }
  .contact-icon {
    width: 30px;
    height: 30px;
    flex: none;
  }
  .contact-icon * { fill: none; stroke: var(--ink-light); stroke-width: 2.2; }
  .contact-icon .solid { fill: var(--ink-light); stroke: none; }
  .contact-icon .flap { stroke: var(--card-black); }
</style>
</head>
<body>
  <main class="business-card">
    <svg class="diagonal-band" viewBox="0 0 1100 628" preserveAspectRatio="none" aria-hidden="true">
      <polygon points="965,0 1100,0 1100,628 330,628"/>
    </svg>

    <div class="brand-mark">
      <div class="brand-square"></div>
      <div class="brand-name">harwick<br>studio</div>
    </div>

    <section class="contact-block">
      <h1 class="company-name">Harwick Studio</h1>

      <div class="contact-row">
        <div class="address-lines">4186 Maplecrest Rd. Unit B-2<br>Brookvale, WY 80317</div>
        <svg class="contact-icon" viewBox="0 0 30 30" aria-hidden="true">
          <path class="solid" d="M15 2c-5.5 0-9.5 4-9.5 9.3C5.5 18 15 28 15 28s9.5-10 9.5-16.7C24.5 6 20.5 2 15 2zm0 13.3a4 4 0 1 1 0-8 4 4 0 0 1 0 8z"/>
        </svg>
      </div>

      <div class="contact-row">
        <span>www.harwickstudio-example.com</span>
        <svg class="contact-icon" viewBox="0 0 30 30" aria-hidden="true">
          <circle cx="15" cy="15" r="12"/>
          <ellipse cx="15" cy="15" rx="5.5" ry="12"/>
          <line x1="3" y1="15" x2="27" y2="15"/>
        </svg>
      </div>

      <div class="contact-row">
        <span>lu@harwickstudio-example.com</span>
        <svg class="contact-icon" viewBox="0 0 30 30" aria-hidden="true">
          <rect class="solid" x="3" y="7" width="24" height="17" rx="1.5"/>
          <polyline class="flap" points="4,8.5 15,17 26,8.5"/>
        </svg>
      </div>
    </section>
  </main>
</body>
</html>
```